Biz Card Design TPVC

New business card for a new company.
Logo was completed by a designer on ArtFlock and looking to continue requesting additional services.
Company Name: Tidal Prime Voltage Collective
Although this company is starting in Canada, we will be moving towards a global presence within the next 6 months.
Key elements to this business are as follows.
Energy Procurement
Energy Reduction Services
Demand Side Consulting
Energy Efficiency Consulting
Saving Clients Money
Helping Them Go "Green"
Managing Their Energy Requirements
Basically the goal for our company is to find the best procurement solution for our clients and reduce their energy consumption. This reduces their expenses and the amount of greenhouse gas they produce on a daily basis.
I have been in the energy footprint for the last 20 years and know that most companies are looking to "do whatever is necessary to get them to sign on the dotted line". I would prefer to walk away from a client that I can't help than to put them into a situation that they will regret for years to come. This is where the "TIDAL" part of the company name comes from.
The following is a catch phrase that encompasses what we do.
"Reducing your carbon footprint & energy bill at the same time!"
The back of the card needs to have this statement along with some sort of illustration. The back is a playground for creative ideas.
The front of the card needs the following.
Logo.
First & Last Name (Gus Marwick)
Title (Energy Warrior)
Phone Number (555) 314-2768
Fax Number (555) 862-4091
Email Address gus@tidalprimevoltage.example
Address 47 Orchard Lane Toronto Ontario K4P 2Z7
I want it to be a card that is remembered when any of my staff give it to a customer. It HAS to stand out.
Target Market(s)
Business Owners, Decision Makers, 30 to 65+
Industry/Entity Type
Business
Look and feel
Each slider illustrates characteristics of the customer's brand and the style your logo design should communicate.

```html
<!DOCTYPE html>
<html lang="en">
<head>
<meta charset="utf-8">
<title>Tidal Prime Voltage Collective – Business Card</title>
<link rel="stylesheet" href="https://fonts.googleapis.com/css2?family=Exo+2:wght@500;700&family=Questrial&display=swap">
<style>
  :root {
    --paper: #ffffff;
    --brand-blue: #3a66b2;
    --green-deep: #00873e;
    --green-light: #cfe59a;
    --sky-deep: #1582c6;
    --sky-light: #c4dbee;
    --band-blue: #1265ad;
    --ink-light: #ffffff;
  }
  html, body {
    margin: 0;
    padding: 0;
    overflow: hidden;
    background: var(--paper);
  }
  .card {
    position: relative;
    width: 1200px;
    height: 686px;
    overflow: hidden;
    background: var(--paper);
    font-family: "Questrial", sans-serif;
  }
  .card-art {
    position: absolute;
    inset: 0;
    width: 1200px;
    height: 686px;
  }
  .brand-name {
    position: absolute;
    right: 42px;
    top: 150px;
    margin: 0;
    font-family: "Exo 2", sans-serif;
    font-weight: 700;
    font-size: 37px;
    letter-spacing: -0.5px;
    color: var(--brand-blue);
    white-space: nowrap;
  }
  .person {
    position: absolute;
    left: 204px;
    top: 322px;
    text-align: center;
    color: var(--ink-light);
  }
  .person-name {
    margin: 0;
    font-family: "Exo 2", sans-serif;
    font-weight: 700;
    font-size: 46px;
    line-height: 1;
    letter-spacing: 1px;
  }
  .person-title {
    margin: 6px 0 0;
    font-family: "Exo 2", sans-serif;
    font-weight: 500;
    font-size: 28px;
    letter-spacing: 2px;
  }
  .contact {
    position: absolute;
    right: 42px;
    top: 512px;
    margin: 0;
    text-align: right;
    color: var(--ink-light);
    font-size: 25px;
    line-height: 34px;
    font-style: normal;
  }
  .contact-label { font-weight: 700; }
  .email {
    position: absolute;
    left: 67px;
    top: 614px;
    margin: 0;
    color: var(--ink-light);
    font-size: 25px;
  }
</style>
</head>
<body>
  <main class="card">
    <svg class="card-art" viewBox="0 0 1200 686" aria-hidden="false">
      <defs>
        <linearGradient id="sky-fill" x1="0" y1="1" x2="1" y2="0">
          <stop offset="0" stop-color="var(--sky-deep)"/>
          <stop offset="0.55" stop-color="var(--sky-deep)"/>
          <stop offset="1" stop-color="var(--sky-light)"/>
        </linearGradient>
        <linearGradient id="leaf-fill" x1="0" y1="0" x2="1" y2="0.7">
          <stop offset="0" stop-color="var(--green-deep)"/>
          <stop offset="1" stop-color="var(--green-light)"/>
        </linearGradient>
      </defs>
      <polygon class="sky-panel" points="812,354 1200,354 1200,686 640,686" fill="url(#sky-fill)"/>
      <path class="leaf-area" role="img" aria-label="Large green leaf illustration"
            d="M0 380 C 180 260, 560 210, 820 356 L 686 600 L 0 600 Z"
            fill="url(#leaf-fill)"/>
      <rect class="email-band" x="0" y="600" width="700" height="62" fill="var(--band-blue)"/>
    </svg>

    <h1 class="brand-name">Tidal Prime Voltage Collective</h1>

    <div class="person">
      <p class="person-name">Gus Marwick</p>
      <p class="person-title">Energy Warrior</p>
    </div>

    <address class="contact">
      47 Orchard Lane Toronto Ontario<br>
      K4P 2Z7<br>
      <span class="contact-label">Ph:</span> (555) 314-2768<br>
      <span class="contact-label">Fax:</span> (555) 862-4091
    </address>

    <p class="email">Email: gus@tidalprimevoltage.example</p>
  </main>
</body>
</html>
```